Business Card Design Project

I need a business card designed that is clean, simple and elegant.
I am a fashion and advertising photographer based in Cape Town and Durban South Africa.
check out my website: www.marlowvance.co.za for ideas
Updates
Hi all,
Thanks for your submissions so far!
Please note:
I want no more than than black, white and/or grey to be used.
I don't want any photos used.
I would like the card to be double sided.
I would like to continue the design similar to the past ones Ive used.
I hope this helps, please send me further questions should you have any.
many thanks!
Marlow
Hi,
Please have a look at the jpg I loaded(called inspiration) which is the direction or inspiration I am aiming at.
Also PLEASE remember NO PHOTOS to be included on the card
many thanks!!
Target Market(s)
You can look at my site to get a better understanding of the audience:
www.marlowvance.co.za
Industry/Entity Type
Advertising
Requirements
Must have
- Clean design which can also be used for a watermark on photographs
perhaps black background with white text/grey
company called: Marlow Vance Photography
Nice to have
- below I have added logos that I have used in the past.
Should not have
- pictures of cameras
tacky elements

```html
<!DOCTYPE html>
<html lang="en">
<head>
<meta charset="utf-8">
<title>Marlow Vance Photography – Business Card</title>
<link rel="stylesheet" href="https://fonts.googleapis.com/css2?family=Cabin:wght@400&display=swap">
<style>
  :root {
    --card-white: #ffffff;
    --band-black: #030303;
    --brand-grey: #7a7a7a;
    --ink: #0a0a0a;
  }
  html, body {
    margin: 0;
    padding: 0;
    width: 1200px;
    height: 667px;
    overflow: hidden;
    background: var(--card-white);
  }
  .card {
    position: relative;
    width: 1200px;
    height: 667px;
    background: var(--card-white);
    font-family: "Cabin", "Gill Sans", sans-serif;
    color: var(--ink);
  }
  .brand-band {
    position: absolute;
    left: 0;
    top: 216px;
    width: 1200px;
    height: 208px;
    background: var(--band-black);
    display: flex;
    align-items: center;
    justify-content: center;
  }
  .brand-name {
    margin: 0;
    text-align: center;
    color: var(--brand-grey);
    font-weight: 400;
    font-size: 30px;
    line-height: 1.2;
    letter-spacing: 0.08em;
    text-transform: uppercase;
  }
  .brand-name span { display: block; }
  .phones {
    position: absolute;
    top: 448px;
    left: 0;
    width: 1200px;
    text-align: center;
    font-size: 38px;
    line-height: 46px;
  }
  .phones p { margin: 0; }
  .email, .website {
    position: absolute;
    top: 546px;
    margin: 0;
    font-size: 38px;
    line-height: 46px;
  }
  .email { left: 99px; }
  .website { right: 87px; }
</style>
</head>
<body>
  <main class="card">
    <section class="brand-band">
      <h1 class="brand-name"><span>Marlow Vance</span><span>Photography</span></h1>
    </section>
    <div class="phones">
      <p class="phone-mobile">+27 (0)82 555 0147</p>
      <p class="phone-office">+27 (0)31 555 0193</p>
    </div>
    <p class="email">marlow@marlowvance.co.za</p>
    <p class="website">www.marlowvance.co.za</p>
  </main>
</body>
</html>
```